Need new Spot UV Business Card design

We are looking for a new business card design incorporating Spot UV in black & white options / versions. See examples files and Tobin Ashgrove Design logo.
You can see our website at www.tobinashgrove.ca. We want something classy but yet modern. We are open to black or black and/or white on white with the spot uv. We are open to portrait or landscape. Size should be standard 3.5" x 2". The front of the card should focus on the logo and name "Tobin Ashgrove" only. Fonts used should be "Open sans" or "PT Sans".

Target Market(s)

Mid to high end

Industry/Entity Type

Business

Contact Information for Business Card

Tobin Velasko
416.382.4417
tobin@tobinashgrove.ca
www.tobinashgrove.ca
4175 Brightwell Blvd. E Suite 308
Mississauga, ON L5T 2K9

Requirements
Must have
• Name & Logo

```html
<!DOCTYPE html>
<html lang="en">
<head>
<meta charset="utf-8">
<title>Tobin Ashgrove Design — Business Card</title>
<link href="https://fonts.googleapis.com/css2?family=Open+Sans:wght@300;400;700&display=swap" rel="stylesheet">
<style>
  :root {
    --canvas: #f2f2f2;
    --card-black: #1f1d1e;
    --card-black-soft: #2b292a;
    --card-white: #ffffff;
    --silver: #cfcfcf;
    --ink: #1a1a1a;
    --ink-soft: #3a3a3a;
    --faint: #e3e3e3;
  }
  * { margin: 0; padding: 0; box-sizing: border-box; }
  html, body {
    width: 1200px; height: 1200px; overflow: hidden;
    background: var(--canvas);
    font-family: "Open Sans", sans-serif;
  }
  .sheet {
    width: 1200px; height: 1200px;
    display: flex; flex-direction: column; align-items: center; justify-content: center;
    gap: 60px;
  }
  .card {
    width: 880px; height: 503px; position: relative;
    box-shadow: 0 6px 20px rgba(0,0,0,0.12);
    overflow: hidden;
  }
  /* Front */
  .card-front { background: var(--card-black); }
  .front-pattern {
    position: absolute; inset: 0;
    background: radial-gradient(ellipse at center, var(--card-black-soft) 0%, var(--card-black) 75%);
  }
  .front-wordmark {
    position: absolute; left: 50%; top: 50%; transform: translate(-50%, -50%);
    display: flex; align-items: center; gap: 26px;
    color: var(--silver);
  }
  .wordmark-square {
    width: 96px; height: 96px; border: 5px solid var(--silver);
  }
  .front-name {
    font-weight: 300; font-size: 64px; letter-spacing: 2px; line-height: 1;
    text-transform: uppercase;
  }
  /* Back */
  .card-back { background: var(--card-white); color: var(--ink); }
  .holder-name {
    position: absolute; right: 50px; top: 52px;
    font-size: 42px; font-weight: 300; color: var(--ink-soft);
  }
  .holder-name strong { font-weight: 700; color: var(--ink); }
  .faint-square {
    position: absolute; left: 150px; top: 110px;
    width: 230px; height: 230px; border: 10px solid var(--faint);
  }
  .contact-list {
    position: absolute; right: 50px; top: 178px;
    list-style: none; text-align: right;
    font-size: 25px; line-height: 38px; color: var(--ink-soft);
  }
  .contact-list li { display: flex; justify-content: flex-end; align-items: center; gap: 10px; }
  .contact-list svg { width: 20px; height: 20px; flex: none; }
  .back-wordmark {
    position: absolute; left: 50px; top: 348px;
    display: flex; align-items: center; gap: 12px;
    font-size: 40px; font-weight: 300; letter-spacing: 1px; line-height: 1;
    text-transform: uppercase; color: var(--ink);
  }
  .back-wordmark .wordmark-square {
    width: 30px; height: 30px; border: 3px solid var(--ink);
  }
  .address {
    position: absolute; left: 50px; top: 402px;
    font-style: normal; font-size: 25px; line-height: 36px; color: var(--ink-soft);
  }
</style>
</head>
<body>
<main class="sheet">
  <section class="card card-front" aria-label="Card front">
    <div class="front-pattern" role="img" aria-label="Spot UV repeating diamond pattern on black"></div>
    <div class="front-wordmark">
      <span class="wordmark-square"></span>
      <span class="front-name">Tobin Ashgrove</span>
    </div>
  </section>

  <section class="card card-back" aria-label="Card back">
    <h1 class="holder-name">Tobin <strong>Velasko</strong></h1>
    <div class="faint-square" aria-hidden="true"></div>
    <ul class="contact-list">
      <li>416.382.4417
        <svg viewBox="0 0 24 24" aria-hidden="true"><path fill="#555" d="M6.6 10.8a15.1 15.1 0 0 0 6.6 6.6l2.2-2.2c.3-.3.7-.4 1-.2 1.1.4 2.3.6 3.6.6.6 0 1 .4 1 1V20c0 .6-.4 1-1 1A17 17 0 0 1 3 4c0-.6.4-1 1-1h3.5c.6 0 1 .4 1 1 0 1.3.2 2.5.6 3.6.1.3 0 .7-.2 1z"/></svg>
      </li>
      <li>tobin@tobinashgrove.ca
        <svg viewBox="0 0 24 24" aria-hidden="true"><rect x="2" y="5" width="20" height="14" rx="1" fill="#555"/><path d="M2 6l10 7 10-7" fill="none" stroke="#fff" stroke-width="1.6"/></svg>
      </li>
      <li>www.tobinashgrove.ca
        <svg viewBox="0 0 24 24" aria-hidden="true"><g fill="none" stroke="#555" stroke-width="1.6"><circle cx="12" cy="12" r="9"/><ellipse cx="12" cy="12" rx="4" ry="9"/><path d="M3 12h18M5 7h14M5 17h14"/></g></svg>
      </li>
    </ul>
    <div class="back-wordmark">
      <span class="wordmark-square"></span>
      <span>Tobin Ashgrove</span>
    </div>
    <address class="address">
      4175 Brightwell Blvd. E Suite 308<br>
      Mississauga, ON L5T 2K9
    </address>
  </section>
</main>
</body>
</html>
```